Hello,
We’re looking for a new WordPress website for Follow The Tide, our company offering unique well-being retreats and workshops.
We currently have a website online (you can consult it : www.followthetide.ch), but we now need to build a new site on WordPress — more flexible, more intuitive to manage, and better aligned with our evolving needs.

What we’re looking for:
A new userfriendly WordPress site, with:
Inspiring, elegant, and modern design
Smooth user experience on desktop and mobile
Innovative design proposals – we want to be inspired !
SEO best practices
Respect of our existing color palette
The final website will need to be set up on our existing hosting provider (details can be shared later)

Pages to Include:
- Home
- Our Story
- Our Stays - with links to 5 individual pages, each describing one of our stays in detail.
- Activities – with potential links to individual descriptive pages
- Agenda
- Our Charter
- The Team
- Contact
- Blog

Required Features:
- Space for photos and videos
- Sections for testimonials and press articles
- Blog/article layout with strong readability
- Easy-to-update backend for future content
- Newsletter sign-up (pop-up and in footer)
- Additional pop-up on/off
- “Request info” buttons
- “Booking request” buttons
- Integration of our 4 pillars - Breathe · Feel · Connect · Experience - in the design (They’re currently in the footer, but we’re open to creative suggestions)

Who we are :
Follow The Tide offers well-being and personal growth stays but with a very different spirit.
We’re not a classic wellness brand. Our approach is professional, joyful, and grounded.
We create spaces where people can take a real break — breathe, slow down, and reconnect with themselves.
During our stays, people are welcomed like friends:
with warmth, respect, and no pressure.
Each program combines practices like breathwork, movement, creativity, coaching, and massages in a relaxed, beautiful setting of the French Alps.
What makes us different:
A friendly and down-to-earth atmosphere
A wide mix of activities.
A mix of inner work and simple pleasures
Private rooms, nourishing food, and shared moments
Time to talk, to laugh, to walk, or just be silent together - and feel free to be yourself
Our guests come to pause.
They leave feeling lighter, aligned, and full of life

```html
<!DOCTYPE html>
<html lang="en">
<head>
<meta charset="utf-8">
<title>Follow The Tide – Well-being Stays</title>
<link rel="stylesheet" href="https://fonts.googleapis.com/css2?family=Poppins:wght@400;500;600;700;800&display=swap">
<style>
:root{
  --navy:#1c3a8f;
  --blue:#24489c;
  --teal:#6cc6bf;
  --teal-dark:#57b5ae;
  --grey-text:#8a8f99;
  --body-text:#6d7280;
  --light:#f4f5f8;
  --bar:#e9e9ea;
  --stay-orange:#f0c07a;
  --stay-teal:#66c9c0;
  --stay-pink:#e05fad;
  --stay-blue:#6b8ee0;
  --stay-red:#f05556;
}
*{margin:0;padding:0;box-sizing:border-box}
html,body{width:1200px;height:4228px;overflow:hidden}
body{position:relative;background:#fff;font-family:'Poppins',sans-serif;color:var(--body-text)}
.abs{position:absolute}
a{color:inherit;text-decoration:none}

/* header */
.topbar{left:328px;top:0;width:872px;height:36px;background:var(--teal);border-bottom-left-radius:18px;display:flex;align-items:center;gap:18px;padding-left:40px;color:#fff;font-size:8.5px}
.topbar .item{display:flex;align-items:center;gap:7px}
.topbar .ico{width:20px;height:20px;border-radius:50%;background:#fff;display:flex;align-items:center;justify-content:center}
.topbar .addr{line-height:1.15;width:200px}
.topbar .follow{margin-left:auto;font-size:11px;font-weight:600;display:flex;align-items:center;gap:8px;padding-right:22px}
.topbar .soc{width:18px;height:18px;border-radius:50%;background:#fff}
.logo{display:flex;align-items:center;gap:10px;color:var(--navy);font-weight:700}
.logo .mark{width:22px;height:22px;border-radius:50%;background:var(--teal)}
.header-logo{left:98px;top:30px;font-size:30px;letter-spacing:.5px}
.nav{left:446px;top:66px;display:flex;gap:21px;align-items:center;font-size:10.5px;font-weight:600;color:var(--teal-dark);text-transform:uppercase}
.btn{display:inline-flex;align-items:center;justify-content:center;border-radius:20px;font-weight:600;text-transform:uppercase;color:#fff}
.btn-contact{left:1006px;top:56px;width:119px;height:38px;background:var(--teal);font-size:11px}

/* hero */
.hero{left:0;top:110px;width:1200px;height:706px}
.hero-title{left:75px;top:282px;color:#fff;font-weight:800;line-height:1}
.hero-title .l1{font-size:108px;letter-spacing:2px;display:block}
.hero-title .l2{font-size:62px;display:block;margin-top:6px}
.hero-text{left:76px;top:480px;width:450px;color:#fff;font-size:10.5px;line-height:16px}

/* history */
.section-h{font-weight:800;font-size:36px;color:var(--navy);line-height:1}
.section-h .t{color:var(--teal)}
.history-h{left:657px;top:956px}
.history-text{left:657px;top:1012px;width:446px;font-size:10.3px;line-height:16.5px;color:var(--grey-text)}
.history-text p{margin-bottom:16.5px}
.btn-read{background:var(--teal);font-size:10px;width:118px;height:38px}
.circle-img{border-radius:50%}

/* pillars */
.pillar{width:174px;text-align:center}
.pillar .disc{width:174px;height:174px;border-radius:50%;background:var(--teal)}
.pillar .disc.dark{background:var(--navy)}
.pillar .lbl{margin-top:22px;font-size:22px;font-weight:700;color:#9a9ea6;letter-spacing:.5px}

/* charter */
.charter-h{left:195px;top:2035px;color:#fff;font-size:35px;font-weight:800}
.charter-sub{left:197px;top:2075px;color:#fff;font-size:13px;font-weight:700}
.charter-text{left:197px;top:2096px;width:326px;color:#fff;font-size:10.3px;line-height:16.5px}
.btn-navy{background:var(--navy);font-size:10px}
.dots{left:210px;top:2272px;display:flex;gap:8px}
.dots span{width:13px;height:13px;border-radius:50%;background:var(--teal-dark);opacity:.7}
.dots span.on{background:#fff;opacity:1}

/* stays */
.stays-h{left:0;width:1200px;top:2534px;text-align:center}
.stay{width:148px;height:148px;border-radius:50%;display:flex;align-items:center;justify-content:center;text-align:center;color:#fff;font-weight:700;font-size:14.5px;line-height:18px;top:2586px}

/* blogs */
.blogs-h{left:0;width:1200px;top:2824px;text-align:center}
.card{top:2890px;width:250px;height:332px;background:#fff;box-shadow:0 4px 18px rgba(30,40,80,.12);border-radius:3px;overflow:hidden}
.card .img{height:153px}
.card .body{padding:16px 18px}
.card .date{font-size:9px;color:var(--navy)}
.card .title{margin-top:7px;font-size:15px;font-weight:600;color:#111;line-height:19px}
.card .excerpt{margin-top:8px;font-size:9.6px;line-height:16px;color:#7b7f88}
.card .more{margin-top:12px;font-size:10px;color:var(--navy)}
.pager{left:533px;top:3251px;display:flex;gap:4px}
.pager span{width:42px;height:3px;background:#c9d5ef}
.pager span.on{background:var(--navy)}

/* testimonial */
.quote-text{left:222px;top:3512px;width:342px;color:#fff;font-size:10.3px;line-height:16.5px}
.stars{left:222px;top:3640px;color:var(--teal);font-size:19px;letter-spacing:1px}
.quote-name{left:222px;top:3674px;color:#fff;font-size:12px;font-weight:700}
.qdash{left:222px;top:3710px;display:flex;gap:9px}
.qdash span{width:24px;height:3px;background:#fff;opacity:.5}
.qdash span.on{opacity:1}

/* footer */
.footer-logo{left:131px;top:4000px;font-size:34px}
.f-h{font-size:15px;font-weight:700;color:var(--navy)}
.f-links{list-style:none;font-size:10.5px;line-height:19px;color:#666;margin-top:8px}
.f-sub{font-size:10px;color:#a6d8d3;margin-top:6px}
.f-input{margin-top:16px;width:218px;height:36px;border:1.5px solid var(--teal);border-radius:18px;display:flex;align-items:center;gap:8px;padding-left:18px;font-size:10.5px;color:#777}
.f-btn{margin-top:9px;width:218px;height:37px;background:var(--navy);font-size:10.5px}
.f-soc{display:flex;gap:11px;margin-top:14px}
.f-soc span{width:36px;height:36px;border-radius:50%;background:var(--navy)}
.bottombar{left:0;top:4179px;width:1200px;height:49px;background:var(--bar);font-size:10.5px;color:#333}
.chat{left:1022px;top:4160px;width:44px;height:44px;border-radius:50%;background:var(--navy);display:flex;align-items:center;justify-content:center}
</style>
</head>
<body>

<!-- header -->
<div class="abs topbar">
  <div class="item"><span class="ico"><svg width="11" height="11" viewBox="0 0 24 24"><path d="M6.6 10.8a15 15 0 0 0 6.6 6.6l2.2-2.2c.3-.3.7-.4 1-.2 1.1.4 2.3.6 3.6.6.6 0 1 .4 1 1V20c0 .6-.4 1-1 1A17 17 0 0 1 3 4c0-.6.4-1 1-1h3.5c.6 0 1 .4 1 1 0 1.3.2 2.5.6 3.6.1.3 0 .7-.2 1z" fill="#1c3a8f"/></svg></span>+41 21 555 01 42</div>
  <div class="item"><span class="ico"><svg width="11" height="11" viewBox="0 0 24 24"><path d="M3 5h18v14H3z" fill="#1c3a8f"/><path d="M3 5l9 7 9-7" stroke="#fff" stroke-width="2" fill="none"/></svg></span>info@followthetide.ch</div>
  <div class="item"><span class="ico"><svg width="11" height="11" viewBox="0 0 24 24"><path d="M3 5h18v14H3z" fill="#1c3a8f"/><path d="M3 5l9 7 9-7" stroke="#fff" stroke-width="2" fill="none"/></svg></span><span class="addr">Follow The Tide Sàrl Chemin des Vagues 8<br>CH - 1000 Lumen</span></div>
  <div class="follow">follow <span class="soc" aria-label="Social profile"></span><span class="soc" aria-label="Social profile"></span><span class="soc" aria-label="Social profile"></span></div>
</div>
<a class="abs logo header-logo" href="#"><span class="mark"></span>Follow The Tide</a>
<nav class="abs nav">
  <svg width="13" height="12" viewBox="0 0 24 22"><path d="M12 1L1 11h3v10h6v-6h4v6h6V11h3z" fill="#1c3a8f"/></svg>
  <a href="#">Our Story</a><a href="#">Our Stays</a><a href="#">Activities</a><a href="#">Agenda</a><a href="#">Our Charter</a><a href="#">The Team</a><a href="#">Blo</a>
</nav>
<a class="abs btn btn-contact" href="#">Contact</a>

<!-- hero -->
<section class="abs hero">
  <svg width="1200" height="706" viewBox="0 0 1200 706" class="abs" style="left:0;top:0">
    <defs>
      <linearGradient id="heroTeal" x1="0" y1="0" x2="1" y2="1"><stop offset="0" stop-color="#7fd0c9"/><stop offset="1" stop-color="#5bbab2"/></linearGradient>
      <radialGradient id="heroPhoto" cx=".5" cy=".45" r=".6"><stop offset="0" stop-color="#e6ecef"/><stop offset=".6" stop-color="#b9c9d0"/><stop offset="1" stop-color="#6f8594"/></radialGradient>
    </defs>
    <rect width="1200" height="706" fill="var(--blue)"/>
    <path d="M880 0H1200V590C1080 640 900 700 740 706C700 600 990 520 920 300C880 190 850 80 880 0Z" fill="url(#heroTeal)" role="img" aria-label="Soft background photo of a woman breathing outdoors"/>
    <path d="M0 588C210 560 430 740 660 706C860 676 1020 600 1200 548V706H0Z" fill="#fff"/>
    <circle cx="821" cy="325" r="262" fill="#3a5fae"/>
    <circle cx="821" cy="325" r="246" fill="url(#heroPhoto)" role="img" aria-label="Photo of a man with eyes closed breathing deeply"/>
    <path d="M516 168l4-14M530 176l10-10M536 190l12-2" stroke="#6cc6bf" stroke-width="2.5" stroke-linecap="round" fill="none"/>
  </svg>
</section>
<h1 class="abs hero-title"><span class="l1">FOLLOW</span><span class="l2">THE TIDE</span></h1>
<p class="abs hero-text">Imagine a space designed to allow for a true break, where every breath counts. Through its retreats, Follow The Tide invites you on an inner and outer journey, a unique experience where each step reconnects you with your vitality and well-being.</p>

<!-- history -->
<div class="abs circle-img" style="left:378px;top:898px;width:164px;height:164px;background:var(--teal)"></div>
<div class="abs circle-img" role="img" aria-label="Photo of a senior man resting after a run by a river" style="left:96px;top:926px;width:400px;height:400px;background:radial-gradient(circle at 50% 45%,#c9c2b8,#7a7f7c 70%,#4c5a5f)"></div>
<div class="abs circle-img" role="img" aria-label="Photo of a sunset over a field with dandelion seeds" style="left:332px;top:1191px;width:272px;height:272px;background:radial-gradient(circle at 45% 55%,#f3e6c4,#b9a585 40%,#3b3a2c 85%)"></div>
<h2 class="abs section-h history-h"><span class="t">OUR</span> HISTORY</h2>
<svg class="abs" style="left:896px;top:936px" width="36" height="30"><path d="M6 20l-2-14M14 22l6-12M20 28l12-6" stroke="#1c3a8f" stroke-width="2.2" stroke-linecap="round"/></svg>
<div class="abs history-text">
  <p>Follow The Tide is, above all, a story of men and women, a story of encounters and desire, a desire to share, a desire to refocus and a desire to breathe.</p>
  <p>Absorbed in a world that is running out of time, it has become essential to find a little personal space to take precisely the time we are so desperately running after.</p>
  <p>Through our fiduciary activities at Tide Ahead and Tide Works, we have been able to observe the growing imbalance in most of our lives and the desire was born to create this bubble of respite in a world that is constantly agitated.</p>
  <p>Humans are multiple and complex and it is taking into account all our dimensions that drives us to offer you holistic and well-being programs in a protected, caring and welcoming environment (well… that's our goal 🙂).</p>
  <p>With respect for oneself and others, our programs are open to all, totally inclusive, because we deeply believe in the enrichment of our own consciousness through sharing in the broadest sense of the term.</p>
  <p>And that's why we believe it's important to commit to respecting our fundamentals. The following charter is an integral part of our commitments to each of us, and in this sense, it also commits you to our organization.</p>
</div>
<a class="abs btn btn-read" style="left:657px;top:1392px" href="#">Read More</a>

<!-- pillars -->
<div class="abs pillar" style="left:195px;top:1552px"><div class="disc" role="img" aria-label="Breathe icon with lungs"></div><div class="lbl">BREATHE</div></div>
<div class="abs pillar" style="left:407px;top:1552px"><div class="disc dark" role="img" aria-label="Feel icon with two faces"></div><div class="lbl">FEEL</div></div>
<div class="abs pillar" style="left:619px;top:1552px"><div class="disc" role="img" aria-label="Connect icon with heart and mind"></div><div class="lbl">CONNECT</div></div>
<div class="abs pillar" style="left:829px;top:1552px"><div class="disc" role="img" aria-label="Experience icon with a foot in water"></div><div class="lbl">EXPERIENCE</div></div>

<!-- charter -->
<svg class="abs" style="left:0;top:1860px" width="1200" height="550" viewBox="0 0 1200 550">
  <path d="M0 40C200 10 380 60 560 50C760 40 900 0 1200 30V520C1000 480 800 520 560 500C340 480 180 560 0 500Z" fill="var(--teal)"/>
  <path d="M540 500C620 440 700 420 820 460C950 500 1080 470 1200 520V550H520Z" fill="#8fd3cd" opacity=".55"/>
  <circle cx="805" cy="296" r="200" fill="none" stroke="#fff" stroke-width="1.2" opacity=".8"/>
  <circle cx="805" cy="296" r="190" fill="#c9d8da" role="img" aria-label="Photo of a woman breathing calmly with a hand on her chest"/>
</svg>
<h2 class="abs charter-h">OUR CHARTER</h2>
<div class="abs charter-sub">SHARING AND CONFIDENTIALITY</div>
<p class="abs charter-text">I promise to let everyone express themselves freely and share their opinions and experiences with respect for others and themselves. I promise to respect everyone's privacy and to keep confidential all personal and private information shared in connection with the activities organized by Follow The Tide. What happens in Vegas, stays in Vegas 🙂.</p>
<a class="abs btn btn-navy" style="left:195px;top:2210px;width:117px;height:36px" href="#">Read More</a>
<div class="abs dots"><span></span><span></span><span class="on"></span><span></span><span></span><span></span></div>

<!-- stays -->
<svg class="abs" style="left:0;top:2440px" width="1200" height="460">
  <circle cx="30" cy="120" r="100" fill="none" stroke="#eef0f5" stroke-width="26"/>
  <circle cx="1190" cy="330" r="130" fill="none" stroke="#eef0f5" stroke-width="30"/>
</svg>
<h2 class="abs section-h stays-h"><span class="t">OUR</span> STAYS</h2>
<a class="abs stay" style="left:202px;background:var(--stay-orange)" href="#">INSTANT<br>WORKSHOPS</a>
<a class="abs stay" style="left:363px;background:var(--stay-teal)" href="#">6-NIGHT<br>FLIGHT</a>
<a class="abs stay" style="left:525px;background:var(--stay-pink)" href="#">4-NIGHT<br>GETAWAY</a>
<a class="abs stay" style="left:688px;background:var(--stay-blue)" href="#">2-NIGHT<br>BREAK</a>
<a class="abs stay" style="left:849px;background:var(--stay-red)" href="#">1 DAY<br>BREAK</a>

<!-- blogs -->
<h2 class="abs section-h blogs-h"><span class="t">OUR</span> BLOGS</h2>
<article class="abs card" style="left:204px">
  <div class="img" role="img" aria-label="Photo of hands practising CPR training" style="background:linear-gradient(135deg,#5a5a5e,#8d4a4a)"></div>
  <div class="body"><div class="date">Jull 16, 2025</div><div class="title">Lorem Ipsum is simply dummy text of the printing</div><div class="excerpt">Learn how equipping your team with CPR skills can create a safer work environment and potentially...</div><div class="more">Read More ›</div></div>
</article>
<article class="abs card" style="left:476px">
  <div class="img" role="img" aria-label="Photo of a first aid trainer with a mannequin" style="background:linear-gradient(135deg,#7d8a94,#c8c4bd)"></div>
  <div class="body"><div class="date">Jull 16, 2025</div><div class="title">Lorem Ipsum is simply dummy text of the printing</div><div class="excerpt">Discover the essential information about Automated External Defibrillators, including their importance, proper...</div><div class="more">Read More ›</div></div>
</article>
<article class="abs card" style="left:747px">
  <div class="img" role="img" aria-label="Photo of a group practising first aid on mannequins" style="background:linear-gradient(135deg,#6c6a66,#b8a99a)"></div>
  <div class="body"><div class="date">Jull 16, 2025</div><div class="title">Lorem Ipsum is simply dummy text of the printing</div><div class="excerpt">A comprehensive checklist of essential first aid supplies to ensure your workplace is prepared for any...</div><div class="more">Read More</div></div>
</article>
<div class="abs pager"><span class="on"></span><span></span><span></span></div>

<!-- testimonial -->
<svg class="abs" style="left:0;top:3320px" width="1200" height="490" viewBox="0 0 1200 490">
  <defs><linearGradient id="testiBlue" x1="0" y1="0" x2="1" y2="0"><stop offset="0" stop-color="#24489c"/><stop offset="1" stop-color="#2d56ad"/></linearGradient></defs>
  <path d="M0 30C260 0 520 60 760 40C960 20 1080 0 1200 20V420C1000 470 760 440 540 460C330 480 160 430 0 470Z" fill="url(#testiBlue)"/>
  <circle cx="800" cy="260" r="190" fill="#4f79c6" opacity=".8"/>
  <circle cx="795" cy="260" r="180" fill="#d9d6d3" role="img" aria-label="Photo of a smiling woman waving"/>
  <circle cx="673" cy="391" r="40" fill="#fff"/>
  <circle cx="673" cy="391" r="35" fill="var(--navy)"/>
  <path d="M667 381v20l16-10z" fill="#fff"/>
  <g fill="var(--teal)">
    <circle cx="368" cy="138" r="30"/><path d="M340 140C340 110 360 90 386 84L380 100C368 104 362 114 362 126Z"/>
    <circle cx="430" cy="138" r="30"/><path d="M402 140C402 110 422 90 448 84L442 100C430 104 424 114 424 126Z"/>
  </g>
</svg>
<p class="abs quote-text">Lorem Ipsum is simply dummy text of the printing and typesetting industry. Lorem Ipsum has been the industry's standard dummy text ever since the 1500s, when an unknown printer took a galley of type and scrambled it to make a type specimen book. It has survived not only five centuries, but also the leap into electronic typesetting, remaining essentially unchanged. It was popularised in the 1960s with the release of Letraset sheets containing Lorem</p>
<div class="abs stars">★★★★★</div>
<div class="abs quote-name">LENA &amp; MARC</div>
<div class="abs qdash"><span class="on"></span><span></span><span></span></div>

<!-- footer -->
<div class="abs logo footer-logo"><span class="mark"></span>Follow The Tide</div>
<div class="abs" style="left:456px;top:3946px">
  <div class="f-h">QUICK LINKS</div>
  <ul class="f-links"><li>Home</li><li>Our Story</li><li>Our Stays</li><li>Activities</li><li>Agenda</li><li>Our Charter</li><li>The Team</li><li>Blo</li><li>Contact</li></ul>
</div>
<div class="abs" style="left:637px;top:3946px">
  <div class="f-h">NEWSLETTER SIGNUP</div>
  <div class="f-sub">Subscribe our newsletter</div>
  <div class="f-input"><svg width="12" height="10" viewBox="0 0 24 20"><rect x="1" y="1" width="22" height="18" fill="none" stroke="#888" stroke-width="2"/><path d="M1 1l11 9 11-9" fill="none" stroke="#888" stroke-width="2"/></svg>Enter email address</div>
  <a class="btn f-btn" href="#">Read More</a>
</div>
<div class="abs" style="left:892px;top:3946px">
  <div class="f-h">SOCIAL MEDIA</div>
  <div class="f-soc"><span aria-label="Social profile"></span><span aria-label="Social profile"></span><span aria-label="Social profile"></span></div>
</div>
<div class="abs bottombar">
  <div class="abs" style="left:472px;top:18px">© 2024 Open Shore Studio, All Rights Reserved</div>
  <div class="abs" style="left:813px;top:18px;color:#777">Privacy Policy &nbsp;|&nbsp; Terms of Service</div>
</div>
<div class="abs chat"><svg width="22" height="20" viewBox="0 0 24 22"><path d="M3 3h18v12H9l-5 4v-4H3z" fill="#fff"/><circle cx="8" cy="9" r="1.4" fill="#1c3a8f"/><circle cx="12" cy="9" r="1.4" fill="#1c3a8f"/><circle cx="16" cy="9" r="1.4" fill="#1c3a8f"/></svg></div>

</body>
</html>
```